Peter Lanford Studios Business Card

Looking for a clear, modern, elegant, sharp business card that conveys a professional yet edgy image to my business as a wedding, portrait, and travel photographer. Would like something that looks vintage yet modern. Need a new business card to grow my business. We are growing the business for Wedding and Event Photography as well as fine art Photography. (Mostly Landscapes)
Updates

I’m looking through designs now but I have a new logo that i want using please.

New logo uploaded please redesign using that

PLEASE ALL DESIGNERS LOOK IN BRIEF FOR NEW LOGO

Target Market(s)

Brides, Grooms, Families with Kids, People looking for Fine Art Photography Artwork

Industry/Entity Type

Photographer

Contact Information for Business Card

Unsure

Font styles to use
Serif

Colors

Designer to choose colors to be used in the design.

Requirements
Must have
• My Website:
• http://lanfordgallery.snapfolio.example
• Phone:
• 555-418-2061
• Email:
• petelanfordgallery@mailbox.example
Nice to have
• Would like a sort of shine on the printing finish.
• I like black I think it looks good on a business card.
• Can try working with my logo (png that I've attached)

```html
<!DOCTYPE html>
<html lang="en">
<head>
<meta charset="utf-8">
<title>Peter Lanford Studios — Business Card</title>
<link rel="stylesheet" href="https://fonts.googleapis.com/css2?family=Josefin+Sans:wght@300;400&family=Lato:wght@400&display=swap">
<style>
  :root {
    --backdrop: #e6e3de;
    --card: #050505;
    --ink: #f2f2f2;
    --ink-soft: #d9d9d9;
    --rule: #e8e8e8;
    --band: #8a8a8a;
  }
  * { box-sizing: border-box; margin: 0; padding: 0; }
  html, body {
    width: 1200px;
    height: 800px;
    overflow: hidden;
    background: var(--backdrop);
  }
  .sheet {
    position: relative;
    width: 1200px;
    height: 800px;
    display: flex;
    align-items: center;
    justify-content: center;
    gap: 60px;
  }
  .card {
    position: relative;
    width: 520px;
    height: 297px;
    background: var(--card);
    color: var(--ink);
    overflow: hidden;
    box-shadow: 0 10px 24px rgba(0,0,0,0.22);
  }

  /* Back side: contact details */
  .card-back .contact {
    position: absolute;
    top: 86px;
    left: 0;
    right: 0;
    text-align: center;
    font-family: 'Lato', sans-serif;
    font-size: 15px;
    line-height: 1.55;
    letter-spacing: 0.04em;
    color: var(--ink-soft);
    list-style: none;
  }
  .card-back .accent-rule {
    position: absolute;
    right: 0;
    top: 66px;
    width: 60px;
    height: 1.5px;
    background: var(--rule);
  }
  .card-back .base-rule {
    position: absolute;
    left: 0;
    right: 0;
    height: 1.5px;
    background: var(--rule);
  }
  .card-back .base-rule.upper { top: 228px; }
  .card-back .base-rule.lower { top: 272px; }

  /* Front side: identity */
  .card-front .mark {
    position: absolute;
    top: 52px;
    left: 50%;
    width: 62px;
    height: 62px;
    margin-left: -31px;
    border: 1.5px solid var(--ink);
  }
  .card-front .studio-name {
    position: absolute;
    top: 128px;
    left: 0;
    right: 0;
    text-align: center;
    font-family: 'Josefin Sans', sans-serif;
    font-weight: 300;
    color: var(--ink);
  }
  .card-front .studio-name .name {
    display: block;
    font-size: 36px;
    letter-spacing: 0.02em;
    line-height: 1.1;
  }
  .card-front .studio-name .label {
    display: block;
    font-size: 15px;
    letter-spacing: 0.55em;
    padding-left: 0.55em;
    margin-top: 4px;
  }
  .card-front .stripe-band {
    position: absolute;
    left: 0;
    right: 0;
    bottom: 14px;
    height: 16px;
    background: var(--band);
  }
</style>
</head>
<body>
  <main class="sheet">
    <section class="card card-back" aria-label="Card back">
      <span class="accent-rule"></span>
      <ul class="contact">
        <li>lanfordgallery.snapfolio.example</li>
        <li>555-418-2061</li>
        <li>petelanfordgallery@mailbox.example</li>
      </ul>
      <span class="base-rule upper"></span>
      <span class="base-rule lower"></span>
    </section>

    <section class="card card-front" aria-label="Card front">
      <span class="mark"></span>
      <h1 class="studio-name">
        <span class="name">PETER LANFORD</span>
        <span class="label">STUDIOS</span>
      </h1>
      <div class="stripe-band" role="img" aria-label="Diagonal black and white stripe band along the lower edge"></div>
    </section>
  </main>
</body>
</html>
```